BrivoMetra. Lantern for the Enterprise Worth. Business card

Professional business card for BrivoMetra (Lantern for the Enterprise Worth)
My rationale: Strategy-> Execution-> Results-> Value that lead to the BrivoMetra name: We put the Lantern for the Enterprise Worth.
We deliver value to our customers helping them at defining a good strategy (cyan arrow). 90% of well formulated strategies fail due to poor execution so we also consider strategical execution very important (green arrow). Due to the execution we obtain the results (blue arrow). Finally, the results provide feedback to redefine strategy, and the new strategy has to be executed and new results obtained providing new feedback and on and on. It's like a wheel that finally, must create corporate value: value for shareholders, staholders, employees, providers...-

Target Market(s)

CEOs and steering comitees , invewrnent funds

Industry/Entity Type

Business Consultant

Contact Information for Business Card

Teodoro Vinschetti
CEO & Founder
teodoro.vinschetti@brivometra-example.com
Mobile: +34 655.802.913
www.brivometra-example.com

Colors

Designer to choose colors to be used in the design.

Requirements
Nice to have
• Nice to hace the words: Strategy, execution, results
• Nice to vave the claim: Lantern for the Enterprise Worth
• The three colors should be shown:
• cyan for STRATEGY
• green for EXECUTION
• blue for RESULTS
Should not have
• Complete black background

```html
<!DOCTYPE html>
<html lang="en">
<head>
<meta charset="utf-8">
<title>BrivoMetra – Business Card</title>
<link rel="stylesheet" href="https://fonts.googleapis.com/css2?family=Open+Sans:wght@400;600;700;800&display=swap">
<style>
  :root {
    --brand-blue: #023399;
    --brand-green: #8cc63f;
    --brand-cyan: #29abe2;
    --card-white: #ffffff;
    --ink: #333a45;
    --rule: #d6d9de;
    --backdrop: #e9e6e3;
  }
  * { box-sizing: border-box; margin: 0; padding: 0; }
  html, body {
    width: 1200px; height: 997px; overflow: hidden;
    background: var(--backdrop);
    font-family: "Open Sans", Arial, sans-serif;
  }
  .canvas { position: relative; width: 1200px; height: 997px; }
  .card {
    position: absolute; width: 560px; height: 320px; overflow: hidden;
    border-radius: 3px;
    box-shadow: 0 6px 18px rgba(0,0,0,.12);
  }
  .card--front { left: 70px; top: 150px; background: var(--card-white); }
  .card--back  { left: 570px; top: 527px; background: var(--brand-blue); }

  .wordmark { display: flex; align-items: center; gap: 10px; font-weight: 800; letter-spacing: -0.5px; white-space: nowrap; }
  .wordmark__dot { border-radius: 50%; flex: none; }

  .card--front .wordmark { position: absolute; left: 30px; top: 124px; font-size: 34px; color: var(--brand-blue); }
  .card--front .wordmark__dot { width: 20px; height: 20px; background: var(--brand-cyan); }

  .divider { position: absolute; left: 272px; top: 40px; width: 1px; height: 120px; background: var(--rule); }

  .contact { position: absolute; left: 288px; top: 40px; color: var(--ink); }
  .contact__name { font-size: 19px; font-weight: 700; color: var(--brand-blue); line-height: 1.2; }
  .contact__role { font-size: 13px; margin-bottom: 12px; }
  .contact__list { list-style: none; font-size: 11px; line-height: 1.7; }
  .contact__list li { display: flex; align-items: center; gap: 8px; white-space: nowrap; }
  .contact__list svg { width: 10px; height: 10px; flex: none; fill: var(--brand-blue); }

  .band {
    position: absolute; right: 0; bottom: 0; height: 34px;
    display: flex; align-items: center; padding: 0 28px;
    font-size: 14px; white-space: nowrap;
  }
  .card--front .band { width: 300px; background: var(--brand-blue); color: var(--card-white); justify-content: center; }
  .card--back .band { width: 440px; background: var(--card-white); font-weight: 700; }

  .card--back .wordmark {
    position: absolute; left: 0; right: 0; top: 125px; justify-content: center;
    font-size: 50px; color: var(--card-white);
  }
  .card--back .wordmark__dot { width: 28px; height: 28px; background: var(--card-white); }
  .pillars .strategy { color: var(--brand-cyan); }
  .pillars .execution { color: var(--brand-green); }
  .pillars .results { color: var(--brand-blue); }
  .pillars .sep { color: var(--brand-green); }
</style>
</head>
<body>
<main class="canvas">

  <section class="card card--front" aria-label="Business card front">
    <div class="wordmark"><span class="wordmark__dot"></span>BrivoMetra</div>
    <div class="divider"></div>
    <div class="contact">
      <p class="contact__name">Teodoro Vinschetti</p>
      <p class="contact__role">CEO &amp; Founder</p>
      <ul class="contact__list">
        <li><svg viewBox="0 0 10 10"><path d="M2.5 0h5a1 1 0 0 1 1 1v8a1 1 0 0 1-1 1h-5a1 1 0 0 1-1-1V1a1 1 0 0 1 1-1zm.5 1.5v6h4v-6z"/></svg>+34 655.802.913</li>
        <li><svg viewBox="0 0 10 10"><path d="M0 2h10v6H0zm1 1v.3l4 2.4 4-2.4V3z"/></svg>teodoro.vinschetti@brivometra-example.com</li>
        <li><svg viewBox="0 0 10 10"><path d="M5 0a5 5 0 1 0 0 10A5 5 0 0 0 5 0zm0 1c.6.7 1 1.9 1.1 3.5H3.9C4 2.9 4.4 1.7 5 1zM1.1 5.5h1.8c.1 1.3.4 2.4.9 3.2A4 4 0 0 1 1.1 5.5zm0-1A4 4 0 0 1 3.8 1.3c-.5.8-.8 1.9-.9 3.2zm2.8 1h2.2C6 7.1 5.6 8.3 5 9c-.6-.7-1-1.9-1.1-3.5zm3.2 0h1.8a4 4 0 0 1-2.7 3.2c.5-.8.8-1.9.9-3.2zm0-1c-.1-1.3-.4-2.4-.9-3.2a4 4 0 0 1 2.7 3.2z"/></svg>www.brivometra-example.com</li>
      </ul>
    </div>
    <p class="band tagline">Lantern for the Enterprise Worth</p>
  </section>

  <section class="card card--back" aria-label="Business card back">
    <div class="wordmark"><span class="wordmark__dot"></span>BrivoMetra</div>
    <p class="band pillars">
      <span class="strategy">Strategy</span><span class="sep">&nbsp;-&nbsp;</span><span class="execution">Execution</span><span class="sep">&nbsp;-&nbsp;</span><span class="results">Results</span>
    </p>
  </section>

</main>
</body>
</html>
```